Slide Master for Halvern Engines - A Systematic Hedge Fund

We are looking for someone to produce a theme and slide master for us for our investor presentations. I have uploaded a few examples of templates that we would like to have included:
Main Title
Section Title
Slides with just bullet points
Different image/table configurations with bullet points and foot notes
Biographies of different lengths
A disclaimer (no one will read this but it should still look nice and needs to be in the presentations)
I have also uploaded the company logo, business card and colour definitions. Currently we have a blue colour scheme defined, but it would be nice to get a complementary set of colours so that when we have charts with more elements we can just draw from those.
The most important thing is that the slide master must be of general use to us. We arn't looking to have a specific presentation designed for us, but a theme/style that we can apply ourselves to any presentation we need to give in the future. It should have clearly defined guidelines for where content should go (and if this is different with and without footnotes for example). We would also like it to have a similar feel to the logo/business cards, so matt colours, high contrast, but not busy.
I'm excited to see the results!

```html
<!DOCTYPE html>
<html lang="en">
<head>
<meta charset="utf-8">
<title>Halvern Engines – Slide Master</title>
<link rel="stylesheet" href="https://fonts.googleapis.com/css2?family=Montserrat:wght@600;700&family=Questrial&display=swap">
<style>
:root{
  --navy:#0b3d6e;
  --blue:#4a8fd9;
  --sky:#a9c4f0;
  --band:#d9e7ea;
  --ink:#1d2a3a;
  --charcoal:#222;
  --grey:#8a8f96;
  --line:#b7bcc2;
  --canvas:#e6e6e6;
}
*{box-sizing:border-box;margin:0;padding:0}
html,body{width:1200px;height:1200px;overflow:hidden;background:var(--canvas);font-family:"Questrial",sans-serif;color:var(--ink)}
.board{position:relative;width:1200px;height:1200px;border:1px solid #999}
.slide{position:absolute;overflow:hidden;border:1px solid #cfd3d7;
  background:radial-gradient(circle at 20% 85%,#eceef0 0,transparent 40%),radial-gradient(circle at 85% 20%,#eef0f2 0,transparent 40%),#fbfbfc}
.abs{position:absolute}
.titlebar{position:absolute;left:7px;top:11px;height:24px;background:var(--navy);border-radius:12px;
  color:#fff;font-family:"Montserrat",sans-serif;font-weight:600;font-size:15px;letter-spacing:.9px;line-height:24px;padding-left:23px;white-space:nowrap}
.subband{position:absolute;background:var(--band);color:var(--navy);font-size:12px;line-height:16px;padding-left:6px}
.box{position:absolute;border:1px dotted #8c96a0}
.hint{font-size:6px;color:var(--navy);padding:3px 4px}
.bullet{font-size:10px;color:var(--navy);padding:3px 4px}
.hdr{position:absolute;height:14px;color:#fff;font-size:9.5px;line-height:14px;padding-left:4px;
  clip-path:polygon(0 0,calc(100% - 8px) 0,100% 50%,calc(100% - 8px) 100%,0 100%)}
.hdr.dark{background:linear-gradient(90deg,#111,#444)}
.hdr.navy{background:linear-gradient(90deg,#0a3563,#1b5a96)}
.hdr.bright{background:linear-gradient(90deg,#3b7fd0,#6ea6e6)}
.hdr-frame{position:absolute;height:14px;border:1px solid #c5cbd1}
.date{position:absolute;font-size:6px;color:var(--grey)}
.note{position:absolute;font-size:3.5px;color:var(--navy)}
.mark{position:absolute;font-size:7px;color:var(--navy);letter-spacing:.4px;white-space:nowrap;display:flex;align-items:center;gap:3px}
.mark::before{content:"";width:5px;height:5px;background:var(--navy)}
.icons{position:absolute;width:90px;height:40px}
.small{font-size:6px;color:var(--navy)}
</style>
</head>
<body>
<svg width="0" height="0" style="position:absolute">
  <defs>
    <symbol id="content-icons" viewBox="0 0 90 40">
      <g fill="none" stroke="#9aa3ad" stroke-width=".7">
        <rect x="1" y="2" width="9" height="7"/><path d="M1 4.5h9M1 7h9M4 2v7M7 2v7"/>
      </g>
      <g><rect x="24" y="5" width="2" height="4" fill="#e6b84a"/><rect x="27" y="2" width="2" height="7" fill="#6f9fd6"/><rect x="30" y="4" width="2" height="5" fill="#e6b84a"/></g>
      <g><rect x="47" y="2" width="7" height="4" fill="#8fbf8a"/><rect x="49" y="5" width="7" height="4" fill="none" stroke="#9aa3ad" stroke-width=".7"/></g>
      <g fill="none" stroke="#9aa3ad" stroke-width=".7"><path d="M70 3l4-2 4 2v4l-4 2-4-2z"/><circle cx="78" cy="8" r="2" stroke="#6f9fd6"/></g>
      <g fill="none" stroke="#9aa3ad" stroke-width=".7"><rect x="1" y="25" width="9" height="7"/><rect x="5" y="28" width="5" height="4" stroke="#6f9fd6"/></g>
      <g fill="none" stroke="#9aa3ad" stroke-width=".7"><rect x="24" y="25" width="9" height="7"/><circle cx="31" cy="31" r="2" stroke="#6f9fd6"/></g>
      <g fill="none" stroke="#9aa3ad" stroke-width=".7"><rect x="47" y="26" width="9" height="6"/><path d="M47 27.5h9M47 30.5h9"/></g>
      <g fill="#9aa3ad"><path d="M71 30c2-4 5-5 7-4-1 1-2 3-1 5-2 0-4 0-6-1z"/><circle cx="77" cy="25" r="1.3" fill="#6f9fd6"/></g>
    </symbol>
    <symbol id="bar-chart" viewBox="0 0 200 130">
      <g stroke="#cfe0ea" stroke-width=".5">
        <path d="M20 5h176M20 14.4h176M20 23.8h176M20 33.2h176M20 42.6h176M20 52h176M20 61.4h176M20 70.8h176M20 80.2h176M20 89.6h176M20 99h176"/>
      </g>
      <g font-size="5" fill="#4a8fd9" text-anchor="end" font-family="Questrial, sans-serif">
        <text x="14" y="7">5</text><text x="14" y="16">4.5</text><text x="14" y="26">4</text><text x="14" y="35">3.5</text><text x="14" y="45">3</text><text x="14" y="54">2.5</text><text x="14" y="63">2</text><text x="14" y="73">1.5</text><text x="14" y="82">1</text><text x="14" y="92">0.5</text><text x="14" y="101">0</text>
      </g>
      <g>
        <rect x="27" y="18" width="6" height="81" fill="#0b3d6e"/><rect x="33" y="54" width="6" height="45" fill="#4a8fd9"/><rect x="39" y="61" width="6" height="38" fill="#b5cfd6"/><rect x="45" y="61" width="6" height="38" fill="#111"/><rect x="51" y="80" width="6" height="19" fill="#2b2b2b"/>
        <rect x="71" y="52" width="6" height="47" fill="#0b3d6e"/><rect x="77" y="16" width="6" height="83" fill="#4a8fd9"/><rect x="83" y="61" width="6" height="38" fill="#b5cfd6"/><rect x="89" y="43" width="6" height="56" fill="#111"/><rect x="95" y="61" width="6" height="38" fill="#2b2b2b"/>
        <rect x="115" y="33" width="6" height="66" fill="#0b3d6e"/><rect x="121" y="65" width="6" height="34" fill="#4a8fd9"/><rect x="127" y="43" width="6" height="56" fill="#b5cfd6"/><rect x="133" y="80" width="6" height="19" fill="#111"/><rect x="139" y="80" width="6" height="19" fill="#2b2b2b"/>
        <rect x="159" y="14" width="6" height="85" fill="#0b3d6e"/><rect x="165" y="46" width="6" height="53" fill="#4a8fd9"/><rect x="171" y="5" width="6" height="94" fill="#b5cfd6"/><rect x="177" y="80" width="6" height="19" fill="#111"/><rect x="183" y="71" width="6" height="28" fill="#2b2b2b"/>
      </g>
      <g font-size="5" fill="#4a8fd9" text-anchor="middle" font-family="Questrial, sans-serif">
        <text x="42" y="110">Category 1</text><text x="86" y="110">Category 2</text><text x="130" y="110">Category 3</text><text x="174" y="110">Category 4</text>
      </g>
      <g font-size="4.5" fill="#4a8fd9" font-family="Questrial, sans-serif">
        <rect x="30" y="119" width="3" height="3" fill="#0b3d6e"/><text x="34" y="122">Series 1</text>
        <rect x="60" y="119" width="3" height="3" fill="#4a8fd9"/><text x="64" y="122">Series 2</text>
        <rect x="90" y="119" width="3" height="3" fill="#b5cfd6"/><text x="94" y="122">Series 3</text>
        <rect x="120" y="119" width="3" height="3" fill="#111"/><text x="124" y="122">Series 4</text>
        <rect x="150" y="119" width="3" height="3" fill="#2b2b2b"/><text x="154" y="122">Series 5</text>
      </g>
    </symbol>
  </defs>
</svg>

<main class="board">

  <!-- Main title -->
  <section class="slide" style="left:66px;top:15px;width:493px;height:285px">
    <div class="abs" style="left:0;right:0;top:110px;text-align:center;font-family:'Questrial',sans-serif;color:var(--navy);font-size:30px;letter-spacing:2px;line-height:30px">HALVERN<br>ENGINES</div>
    <div class="abs" style="left:0;right:0;top:185px;text-align:center;font-size:11px;color:var(--navy)">Sub Title</div>
  </section>

  <!-- Disclaimer -->
  <section class="slide" style="left:630px;top:14px;width:510px;height:286px">
    <div class="titlebar" style="width:497px">Disclaimer</div>
    <div class="box" style="left:14px;top:47px;width:157px;height:211px"><div class="hint">Click to add text</div></div>
    <div class="box" style="left:175px;top:47px;width:157px;height:211px"><div class="hint">Click to add text</div></div>
    <div class="box" style="left:337px;top:47px;width:157px;height:211px"><div class="hint">Click to add text</div></div>
    <svg class="icons" style="left:50px;top:131px"><use href="#content-icons"/></svg>
    <svg class="icons" style="left:211px;top:131px"><use href="#content-icons"/></svg>
    <svg class="icons" style="left:373px;top:131px"><use href="#content-icons"/></svg>
    <div class="date" style="left:39px;top:270px">6 June 2021</div>
    <div class="mark" style="left:400px;top:268px">HALVERN ENGINES</div>
  </section>

  <!-- Title only -->
  <section class="slide" style="left:65px;top:315px;width:495px;height:278px">
    <div class="abs" style="left:33px;top:138px;width:427px;height:39px;background:linear-gradient(180deg,#b8d0f5,var(--sky));border:1px solid #8fb0e6;text-align:center;font-family:'Montserrat',sans-serif;font-weight:700;font-size:25px;line-height:37px;color:#3a3a3a">Click to add title</div>
    <div class="date" style="left:38px;top:264px">6 June 2021</div>
    <div class="mark" style="left:385px;top:262px">HALVERN ENGINES</div>
  </section>

  <!-- Section with two headers -->
  <section class="slide" style="left:630px;top:311px;width:510px;height:287px">
    <div class="titlebar" style="width:497px">Section Title style</div>
    <div class="subband" style="left:26px;top:35px;width:455px;height:17px">Subsection title style</div>
    <div class="hdr-frame" style="left:35px;top:58px;width:226px"></div>
    <div class="hdr dark" style="left:35px;top:58px;width:172px">A Header</div>
    <div class="box" style="left:35px;top:76px;width:441px;height:76px"><div class="bullet">◉Click to add text</div></div>
    <svg class="icons" style="left:215px;top:93px"><use href="#content-icons"/></svg>
    <div class="hdr-frame" style="left:35px;top:158px;width:226px"></div>
    <div class="hdr dark" style="left:35px;top:158px;width:172px">A Second Header</div>
    <div class="box" style="left:35px;top:176px;width:441px;height:76px"><div class="bullet">◉Click to add text</div></div>
    <svg class="icons" style="left:215px;top:193px"><use href="#content-icons"/></svg>
    <div class="date" style="left:39px;top:270px">6 June 2021</div>
    <div class="mark" style="left:400px;top:268px">HALVERN ENGINES</div>
  </section>

  <!-- Section with bar charts -->
  <section class="slide" style="left:65px;top:604px;width:504px;height:284px">
    <div class="titlebar" style="width:491px">Another Section Title style</div>
    <div class="subband" style="left:27px;top:35px;width:449px;height:17px">Section Footnote*</div>
    <div class="box" style="left:33px;top:61px;width:442px;height:40px"><div class="hint">A description of the chart</div></div>
    <svg class="icons" style="left:213px;top:73px;height:20px;overflow:hidden"><use href="#content-icons"/></svg>
    <div class="abs small" style="left:60px;top:109px;width:150px;text-align:center;font-size:8px;color:var(--blue)">Bar Chart Title</div>
    <div class="abs small" style="left:277px;top:109px;width:150px;text-align:center;font-size:8px;color:var(--blue)">Another Bar Chart Title</div>
    <svg class="abs" style="left:30px;top:126px" width="200" height="130"><use href="#bar-chart"/></svg>
    <svg class="abs" style="left:247px;top:126px" width="200" height="130"><use href="#bar-chart"/></svg>
    <div class="date" style="left:38px;top:268px">6 June 2021</div>
    <div class="note" style="left:89px;top:274px">Footnote*</div>
    <div class="mark" style="left:392px;top:266px">HALVERN ENGINES</div>
  </section>

  <!-- Section with table -->
  <section class="slide" style="left:626px;top:606px;width:510px;height:287px">
    <div class="titlebar" style="width:497px">Section Title style</div>
    <div class="subband" style="left:26px;top:35px;width:455px;height:17px">Subsection title style</div>
    <div class="abs" style="left:20px;top:73px;font-size:8px;color:var(--navy)">Table Description</div>
    <svg class="abs" style="left:16px;top:88px" width="295" height="140">
      <rect x="0" y="0" width="294" height="15" fill="#b8d0d8"/>
      <g fill="#e9f1f3"><rect y="15" width="294" height="15.5"/><rect y="46" width="294" height="15.5"/><rect y="77" width="294" height="15.5"/><rect y="108" width="294" height="15.5"/></g>
      <g stroke="#4a8fd9" stroke-width=".7" fill="none">
        <rect x=".5" y=".5" width="293" height="138"/>
        <path d="M0 15h294M0 30.5h294M0 46h294M0 61.5h294M0 77h294M0 92.5h294M0 108h294M0 123.5h294"/>
        <path d="M45 0v139M74 0v139M103 0v139M138 0v139M170 0v139M206 0v139M248 0v139"/>
      </g>
      <text x="4" y="10.5" font-size="7" fill="#4a8fd9" font-family="Questrial, sans-serif">Table</text>
    </svg>
    <div class="hdr dark" style="left:316px;top:63px;width:172px">A Header</div>
    <div class="box" style="left:318px;top:83px;width:167px;height:174px"><div class="bullet">◉Click to add text</div></div>
    <svg class="icons" style="left:357px;top:150px"><use href="#content-icons"/></svg>
    <div class="date" style="left:39px;top:273px">6 June 2021</div>
    <div class="note" style="left:89px;top:278px">Footnote*</div>
    <div class="mark" style="left:400px;top:270px">HALVERN ENGINES</div>
  </section>

  <!-- Section with area chart -->
  <section class="slide" style="left:55px;top:897px;width:516px;height:290px">
    <div class="titlebar" style="width:495px;height:25px">Another Section Title style</div>
    <div class="subband" style="left:26px;top:37px;width:434px;height:16px">Section Footnote</div>
    <div class="hdr bright" style="left:35px;top:63px;width:175px;height:15px">A Header</div>
    <div class="box" style="left:35px;top:81px;width:224px;height:40px"><div class="hint">A description of the chart with a footnote*</div></div>
    <svg class="icons" style="left:104px;top:93px;height:20px;overflow:hidden"><use href="#content-icons"/></svg>
    <div class="hdr navy" style="left:35px;top:132px;width:175px;height:15px">Another Header</div>
    <div class="box" style="left:35px;top:150px;width:224px;height:41px"><div class="hint">A description of the chart with another footnote</div></div>
    <svg class="icons" style="left:104px;top:162px;height:20px;overflow:hidden"><use href="#content-icons"/></svg>
    <div class="hdr-frame" style="left:35px;top:200px;width:224px"></div>
    <div class="hdr dark" style="left:35px;top:200px;width:175px;height:15px">Another Header</div>
    <div class="box" style="left:35px;top:218px;width:224px;height:41px"><div class="hint">A description of the chart with another footnote</div></div>
    <svg class="icons" style="left:104px;top:230px;height:20px;overflow:hidden"><use href="#content-icons"/></svg>
    <div class="box" style="left:272px;top:61px;width:223px;height:12px;border-style:solid;border-color:#c5cbd1;font-size:8px;line-height:11px;text-align:center;color:var(--navy)">Title of the chart with second footnote**</div>
    <svg class="abs" style="left:0;top:0" width="516" height="290">
      <g font-size="4" fill="#4a8fd9" font-family="Questrial, sans-serif">
        <rect x="302" y="79" width="4" height="4" fill="#4a84c6"/><text x="309" y="82.5">Contents _ Type</text>
        <rect x="356" y="79" width="4" height="4" fill="#0b3d6e"/><text x="363" y="82.5">Contents _ Type</text>
        <rect x="410" y="79" width="4" height="4" fill="#111"/><text x="417" y="82.5">Contents _ Type</text>
      </g>
      <g stroke="#7aa6d8" stroke-width=".4" stroke-dasharray="2 1"><path d="M279 92h216M279 108h216M279 124h216M279 140h216M279 156h216M279 172h216M279 188h216M279 204h216M279 220h216"/></g>
      <path d="M279 236V133.6L315 133.6L351 146.4L387 111.2L423 130.4L459 124L495 188V236Z" fill="#2b2b2b"/>
      <path d="M279 236V156L315 159.2L351 159.2L387 168.8L423 143.2L459 156L495 124V236Z" fill="#0b3d6e"/>
      <path d="M279 236V156L315 175.2L351 175.2L387 188L423 140L459 156L495 188V236Z" fill="#4a84c6"/>
      <path d="M279 92V236H495" fill="none" stroke="#4a8fd9" stroke-width=".6"/>
      <g font-size="6" fill="#4a8fd9" text-anchor="end" font-family="Questrial, sans-serif">
        <text x="274" y="94">45</text><text x="274" y="110">40</text><text x="274" y="126">35</text><text x="274" y="142">30</text><text x="274" y="158">25</text><text x="274" y="174">20</text><text x="274" y="190">15</text><text x="274" y="206">10</text><text x="274" y="222">5</text><text x="274" y="238">0</text>
      </g>
      <g font-size="6" fill="#4a8fd9" text-anchor="middle" font-family="Questrial, sans-serif">
        <text x="279" y="246">2012</text><text x="315" y="246">2013</text><text x="351" y="246">2014</text><text x="387" y="246">2015</text><text x="423" y="246">2016</text><text x="459" y="246">2017</text><text x="495" y="246">2018</text>
      </g>
    </svg>
    <div class="date" style="left:40px;top:275px">6 June 2021</div>
    <div class="note" style="left:90px;top:276px">Footnote*<br>Footnote**</div>
    <div class="mark" style="left:403px;top:273px">HALVERN ENGINES</div>
  </section>

  <!-- Biographies -->
  <section class="slide" style="left:627px;top:903px;width:509px;height:286px">
    <div class="titlebar" style="width:494px">Heading for Biographies</div>
    <div class="abs" style="left:20px;top:34px;width:52px;height:60px;background:var(--navy);transform:rotate(-4deg)"></div>
    <div class="abs" style="left:15px;top:35px;width:52px;height:62px;background:linear-gradient(160deg,#cfe0f7,#a9c4f0);border:1px solid #6f9fd6;transform:rotate(-8deg);font-size:9px;line-height:10px;padding:8px 6px;color:var(--ink)">Click icon to add picture</div>
    <div class="box" style="left:79px;top:70px;width:168px;height:19px;font-family:'Montserrat',sans-serif;font-weight:700;font-size:10px;line-height:17px;padding-left:4px;color:var(--navy)">Click to edit Name</div>
    <div class="abs" style="left:256px;top:34px;width:52px;height:60px;background:var(--navy);transform:rotate(-4deg)"></div>
    <div class="abs" style="left:251px;top:35px;width:52px;height:62px;background:linear-gradient(160deg,#cfe0f7,#a9c4f0);border:1px solid #6f9fd6;transform:rotate(-8deg);font-size:9px;line-height:10px;padding:8px 6px;color:var(--ink)">Click icon to add picture</div>
    <div class="box" style="left:315px;top:70px;width:171px;height:19px;font-family:'Montserrat',sans-serif;font-weight:700;font-size:10px;line-height:17px;padding-left:4px;color:var(--navy)">Click to edit Name</div>
    <div class="box" style="left:22px;top:104px;width:225px;height:149px"><div class="bullet" style="color:#2d4a6a">Click to add text</div></div>
    <svg class="icons" style="left:92px;top:164px"><use href="#content-icons"/></svg>
    <div class="box" style="left:262px;top:104px;width:225px;height:149px"><div class="bullet" style="color:#2d4a6a">Click to add text</div></div>
    <svg class="icons" style="left:332px;top:164px"><use href="#content-icons"/></svg>
    <div class="date" style="left:39px;top:271px">6 June 2021</div>
    <div class="mark" style="left:397px;top:270px">HALVERN ENGINES</div>
  </section>

</main>
</body>
</html>
```